Rack Card Design for an Ayurvedic Beauty Product Project

Hello, I need to have rack cards. The rack cards would be about 3 products we are showcasing at an event. I am a cosmetic company. I have a logo and basic design ideas. I have attached some product images and info. By no means am I a designer so please excuse my messy AI files. Please feel free to design this as feminine as you like. :)

Target Market(s)

Beauty industry, organic, holistic, ayurveda

Industry/Entity Type

Cosmetic

```html
<!DOCTYPE html>
<html lang="en">
<head>
<meta charset="utf-8">
<title>Velvet Lotus Rack Card</title>
<link href="https://fonts.googleapis.com/css2?family=Quicksand:wght@400;600&family=Catamaran:wght@400;500;600&family=Hind:wght@400;500&display=swap" rel="stylesheet">
<style>
  :root {
    --plum: #7a1a5c;
    --plum-deep: #5e1046;
    --gold: #b8894f;
    --gold-light: #d9b27a;
    --gold-dark: #8f6534;
    --ink: #2b2226;
    --grey: #555055;
    --paper: #ffffff;
    --backdrop: #a9a9ab;
    --cream: #f1e9df;
  }
  * { margin: 0; padding: 0; box-sizing: border-box; }
  html, body { width: 708px; height: 1200px; overflow: hidden; }
  body {
    background: var(--backdrop);
    font-family: "Hind", sans-serif;
    position: relative;
  }
  .card {
    position: absolute;
    top: 252px;
    width: 310px;
    height: 695px;
    background: var(--paper);
    overflow: hidden;
    box-shadow: 6px 8px 18px rgba(0,0,0,0.35);
  }
  .card--front { left: 29px; }
  .card--back { left: 369px; }

  /* Front */
  .portrait {
    position: absolute; left: 0; top: 0; width: 310px; height: 440px;
    background: radial-gradient(ellipse at 55% 40%, #c79a63 0%, #8a6440 38%, #2a2422 70%, #1b1a1c 100%);
  }
  .swoosh { position: absolute; left: 0; top: 330px; width: 310px; height: 150px; }
  .brand-mark {
    position: absolute; left: 36px; top: 400px;
    width: 62px; height: 62px; border-radius: 50%;
    background: linear-gradient(135deg, var(--gold-light), var(--gold-dark));
  }
  .brand-name {
    position: absolute; left: 30px; top: 490px;
    font-family: "Catamaran", sans-serif; font-weight: 600;
    font-size: 11px; letter-spacing: 0.5px; color: var(--gold);
  }
  .intro {
    position: absolute; left: 19px; top: 514px; width: 274px;
    font-size: 8.6px; line-height: 10.9px; color: var(--ink);
    text-align: justify;
  }
  .intro strong { color: var(--gold-dark); font-weight: 500; }
  .phone-pill {
    position: absolute; left: 16px; top: 610px; width: 280px; height: 40px;
    border-radius: 20px;
    background: linear-gradient(90deg, var(--gold-dark), var(--gold-light) 50%, var(--gold-dark));
    display: flex; align-items: center; padding-left: 18px; gap: 10px;
    color: #fff;
    font-family: "Catamaran", sans-serif; font-weight: 500; font-size: 30px;
  }
  .phone-pill svg { width: 24px; height: 24px; flex: none; }

  .footer-band {
    position: absolute; left: 0; bottom: 0; width: 310px; height: 38px;
  }
  .footer-band svg { position: absolute; inset: 0; }
  .web {
    position: absolute; left: 0; right: 0; bottom: 7px;
    display: flex; justify-content: center; align-items: center; gap: 5px;
    color: #fff; font-family: "Hind", sans-serif; font-size: 12px;
  }
  .web svg { width: 9px; height: 9px; }

  /* Back */
  .list-header { position: absolute; left: 0; top: 0; width: 310px; height: 96px; }
  .list-title {
    position: absolute; left: 0; right: 0; top: 16px; text-align: center;
    font-family: "Quicksand", sans-serif; font-weight: 400;
    font-size: 33px; color: var(--gold-light); line-height: 1;
  }
  .list-subtitle {
    position: absolute; left: 0; right: 0; top: 55px; text-align: center;
    font-family: "Catamaran", sans-serif; font-weight: 600;
    font-size: 17px; color: var(--gold-light);
  }
  .product { position: absolute; left: 0; width: 310px; }
  .product--toner { top: 115px; }
  .product--cream { top: 290px; }
  .product--serum { top: 470px; }
  .product-shot {
    position: absolute; left: 34px; top: 4px; width: 74px; height: 150px;
    border-radius: 6px;
    background: linear-gradient(180deg, #8e2a6d 0%, #6e1652 70%, #c9a265 100%);
  }
  .product--cream .product-shot {
    background: linear-gradient(180deg, #7a1a5c 0%, #7a1a5c 40%, #f3eef0 55%, #ddd6da 100%);
  }
  .product-name {
    position: absolute; left: 130px; top: 22px; width: 170px;
    font-family: "Hind", sans-serif; font-weight: 500;
    font-size: 13px; line-height: 16.5px; color: var(--plum);
  }
  .product-copy {
    position: absolute; left: 130px; top: 74px; width: 165px;
    font-size: 8.8px; line-height: 11.8px; color: var(--grey);
  }
  .product--cream .product-copy { top: 92px; }
  .product--serum .product-copy { top: 70px; }
  .divider {
    position: absolute; left: 28px; width: 282px; height: 2px;
    background: linear-gradient(90deg, rgba(216,178,122,0), var(--gold-light) 30%, var(--gold-light));
  }
  .divider--one { top: 275px; }
  .divider--two { top: 460px; }
</style>
</head>
<body>

<section class="card card--front">
  <div class="portrait" role="img" aria-label="Portrait photograph of a model with long wavy blonde hair against a dark background"></div>
  <svg class="swoosh" viewBox="0 0 310 150" preserveAspectRatio="none" aria-hidden="true">
    <path d="M0 12 C70 -4 170 30 310 150 L310 150 L0 150 Z" fill="#ffffff"/>
    <path d="M0 0 C90 -8 190 40 310 122 L310 150 C200 60 90 30 0 40 Z" fill="var(--plum)"/>
    <path d="M0 40 C90 30 200 62 310 150 L310 142 C200 56 90 24 0 34 Z" fill="var(--gold)"/>
    <path d="M0 40 C90 30 200 64 310 150 L0 150 Z" fill="#ffffff"/>
  </svg>
  <div class="brand-mark" aria-hidden="true"></div>
  <div class="brand-name">VELVET LOTUS</div>
  <p class="intro"><strong>Velvet Lotus</strong> curates organic infused products where holistic skin care meets a luxurious experience. Each ingredient is carefully selected; providing Ayurvedic herbs, rich minerals &amp; elements. Stimulating hydration and anti-oxidants to lift, firm and illuminate your skin. We believe in connecting with your inner mantra, stimulating higher vibrations, self-esteem, positive mind and soul. As a brand we work with our experts/suppliers of Ayurveda to ensure that our products meet the quality, wholesome healing that you need.</p>
  <div class="phone-pill">
    <svg viewBox="0 0 24 24" aria-hidden="true">
      <circle cx="12" cy="12" r="10.5" fill="none" stroke="#fff" stroke-width="1.8"/>
      <path d="M8.3 6.5 L10 6.3 L11 9 L9.8 10 C10.4 11.6 12.4 13.6 14 14.2 L15 13 L17.7 14 L17.5 15.7 C17.3 16.6 16.4 17.2 15.4 17 C11 16 8 13 7 8.6 C6.8 7.6 7.4 6.7 8.3 6.5 Z" fill="#fff"/>
    </svg>
    <span>0100-246-810</span>
  </div>
  <div class="footer-band">
    <svg viewBox="0 0 310 38" preserveAspectRatio="none" aria-hidden="true">
      <path d="M18 8 Q155 -6 292 8 L300 38 L10 38 Z" fill="var(--plum)"/>
      <rect x="0" y="35" width="310" height="3" fill="var(--gold-dark)"/>
    </svg>
    <div class="web">
      <svg viewBox="0 0 10 10" aria-hidden="true"><circle cx="5" cy="5" r="4.3" fill="none" stroke="#fff" stroke-width="0.9"/><ellipse cx="5" cy="5" rx="1.9" ry="4.3" fill="none" stroke="#fff" stroke-width="0.8"/><line x1="0.7" y1="5" x2="9.3" y2="5" stroke="#fff" stroke-width="0.8"/></svg>
      <span>www.velvetlotus.com</span>
    </div>
  </div>
</section>

<section class="card card--back">
  <svg class="list-header" viewBox="0 0 310 96" preserveAspectRatio="none" aria-hidden="true">
    <path d="M0 0 L310 0 L310 40 C240 48 190 62 168 80 L155 96 L142 80 C120 62 70 48 0 40 Z" fill="var(--plum)"/>
  </svg>
  <h1 class="list-title">Velvet Lotus</h1>
  <h2 class="list-subtitle">Product List</h2>

  <article class="product product--toner">
    <div class="product-shot" role="img" aria-label="Product photo of a plum toner tube with gold cap"></div>
    <h3 class="product-name">Velvet Lotus Firming and Lifting Breast Toner</h3>
    <p class="product-copy">Using all natural Ayurvedic herbs, our breast toner, prepares the area for maximum absorption, giving you the best results and the most invigorating treatment</p>
  </article>
  <div class="divider divider--one"></div>

  <article class="product product--cream">
    <div class="product-shot" role="img" aria-label="Product photo of a white cream jar with plum label and gold lid"></div>
    <h3 class="product-name">Velvet Lotus Firming and Lifting Breast Cream</h3>
    <p class="product-copy">Using all natural Ayurvedic herbs, our breast cream helps enhance, tighten, and lift your breast</p>
  </article>
  <div class="divider divider--two"></div>

  <article class="product product--serum">
    <div class="product-shot" role="img" aria-label="Product photo of a slim plum serum tube with gold cap"></div>
    <h3 class="product-name">Velvet Lotus Firming and Toning Breast Serum</h3>
    <p class="product-copy">Using all natural Ayurvedic herbs, and a touch of 24k gold, our serum enhances the experience and quality of results when partnered with the Velvet Lotus Firming and Lifting Breast Cream providing an all-day boosting experience</p>
  </article>

  <div class="footer-band">
    <svg viewBox="0 0 310 38" preserveAspectRatio="none" aria-hidden="true">
      <path d="M18 8 Q155 -6 292 8 L300 38 L10 38 Z" fill="var(--plum)"/>
      <rect x="0" y="35" width="310" height="3" fill="var(--gold-dark)"/>
    </svg>
    <div class="web">
      <svg viewBox="0 0 10 10" aria-hidden="true"><circle cx="5" cy="5" r="4.3" fill="none" stroke="#fff" stroke-width="0.9"/><ellipse cx="5" cy="5" rx="1.9" ry="4.3" fill="none" stroke="#fff" stroke-width="0.8"/><line x1="0.7" y1="5" x2="9.3" y2="5" stroke="#fff" stroke-width="0.8"/></svg>
      <span>www.velvetlotus.com</span>
    </div>
  </div>
</section>

</body>
</html>
```